Custom unique Stationary design for Logistics company

We need a custom, unique , elegant and luxurious full stationary design using our new logo, following these guidelines:
1- Business card: double sided, both sides uses the navy blue as the background main color (same as the code of the navy blue used in our logo).
2- envelope and folder: also use the same navy blue as the main background color.
3- book cover( notepad cover) : same thing with the navy blue
4- letterhead: feel free to use the combination of the colors in our logo.
5- rest of the items are up to your creativity

Target Market(s)

corporates and other businesses

Industry/Entity Type

Logistics and heavy machines contractors

Requirements
Must have
• Letterhead, business card, envelope, notepad cover, paper, file
Nice to have
• navy blue to be main background color for business card, envelope, notepad cover

```html
<!DOCTYPE html>
<html lang="en">
<head>
<meta charset="utf-8">
<title>Keelway Freight — Business Card</title>
<link href="https://fonts.googleapis.com/css2?family=Lato:wght@400;700;900&display=swap" rel="stylesheet">
<style>
  :root {
    --backdrop: #b9b9b9;
    --backdrop-light: #cfcfcf;
    --card-navy: #3a6e8e;
    --accent-orange: #e0693f;
    --paper-white: #ffffff;
    --text-light: #eef3f6;
  }
  * { box-sizing: border-box; margin: 0; padding: 0; }
  html, body {
    width: 1200px; height: 900px; overflow: hidden;
  }
  body {
    background: radial-gradient(ellipse at 45% 30%, var(--backdrop-light), var(--backdrop) 75%);
    font-family: "Lato", sans-serif;
    display: flex; align-items: center; justify-content: center; gap: 60px;
  }
  .card {
    position: relative;
    width: 520px; height: 297px;
    background: var(--card-navy);
    color: var(--paper-white);
    overflow: hidden;
  }

  /* Front side */
  .card-front .brand-name {
    position: absolute; left: 0; right: 0; top: 100px;
    text-align: center;
    font-weight: 900; font-size: 40px; letter-spacing: 2px;
    line-height: 1.2;
  }
  .card-front .stripe {
    position: absolute; top: 222px; height: 9px; background: var(--paper-white);
  }
  .card-front .stripe-left { left: 0; width: 243px; }
  .card-front .stripe-right { right: 0; width: 243px; }

  /* Back side */
  .card-back .brand-name {
    position: absolute; right: 40px; top: 48px;
    font-weight: 900; font-size: 26px; letter-spacing: 1px;
    line-height: 1.2;
  }
  .card-back .holder-name {
    position: absolute; left: 40px; top: 152px;
    font-weight: 700; font-size: 19px; letter-spacing: 0.5px;
    line-height: 1.2;
    text-transform: uppercase;
  }
  .card-back .divider {
    position: absolute; left: 40px; right: 40px; top: 180px;
    height: 1.5px; background: var(--accent-orange);
  }
  .card-back .contact-list {
    position: absolute; left: 40px; top: 194px;
    list-style: none; font-size: 12.5px; color: var(--text-light);
  }
  .card-back .contact-list li {
    display: flex; align-items: center; gap: 8px; line-height: 19px;
  }
  .card-back .contact-list svg { width: 10px; height: 10px; flex: none; }
  .card-back .address {
    position: absolute; right: 40px; top: 194px;
    text-align: right; font-style: normal;
    font-size: 13px; line-height: 19px; color: var(--text-light);
  }
</style>
</head>
<body>
  <section class="card card-front" aria-label="Business card front">
    <div class="brand-name">KEELWAY FREIGHT</div>
    <div class="stripe stripe-left"></div>
    <div class="stripe stripe-right"></div>
  </section>

  <section class="card card-back" aria-label="Business card back">
    <div class="brand-name">KEELWAY FREIGHT</div>
    <div class="holder-name">Dana Whitfield</div>
    <div class="divider"></div>
    <ul class="contact-list">
      <li>
        <svg viewBox="0 0 10 10" aria-hidden="true"><path d="M2 0.5 L3.6 2.8 L2.7 3.9 Q4 6.3 6.1 7.3 L7.2 6.4 L9.5 8 L8.3 9.5 Q3.5 9 0.5 1.7 Z" fill="var(--accent-orange)"/></svg>
        +000 000 0000
      </li>
      <li>
        <svg viewBox="0 0 10 10" aria-hidden="true"><rect x="0.5" y="2" width="9" height="6.5" fill="var(--accent-orange)"/><path d="M0.8 2.3 L5 5.6 L9.2 2.3" fill="none" stroke="var(--card-navy)" stroke-width="0.9"/></svg>
        info@keelwayfreight.com
      </li>
      <li>
        <svg viewBox="0 0 10 10" aria-hidden="true"><circle cx="5" cy="5" r="4.5" fill="var(--accent-orange)"/><path d="M0.5 5 H9.5 M5 0.5 Q2 5 5 9.5 M5 0.5 Q8 5 5 9.5" fill="none" stroke="var(--card-navy)" stroke-width="0.8"/></svg>
        www.keelwayfreight.com
      </li>
    </ul>
    <address class="address">421 address line goes here<br>45452 country name</address>
  </section>
</body>
</html>
```